Stationery for Smart Solutions Company

We need a full stationery design for a startup company named: Brivex Smart Solutions. We are a hi-tech company specialized in smart solutions for condominiums, buldings, airports, etc. We provide a full service solution for fiber optics connectivity, perimeter protection, A.I. surveillance cameras, internet of things, sensors, etc.

Our Stationery should have at least / minimum:
- Envelope
- Business Card
- Letterhead
- Cars
- Laneyards
- Badge
- Gifts
- Uniforms

Target Market(s)

Construction, Condominiums, Corporate, Industries

Colors
59FF00
82FF00
B8FF75
E3FFCB
F4FFEA

Requirements
Must have
• a very modern, corporate and hi-tech touch
Nice to have
• Brivex is a disruptive company, so you should think outside-the-box and innovate, user your creativity and surprise us.

```html
<!DOCTYPE html>
<html lang="en">
<head>
<meta charset="utf-8">
<title>Brivex Smart Solutions – Business Card</title>
<link href="https://fonts.googleapis.com/css2?family=Montserrat:wght@400;500;600;800&display=swap" rel="stylesheet">
<style>
  :root {
    --bg: #d9d9db;
    --card: #4d5056;
    --card-dark: #3f4247;
    --lime: #82ff00;
    --lime-bright: #59ff00;
    --white: #ffffff;
    --text-soft: #e6e7e9;
    --rule: #5d6066;
  }
  * { box-sizing: border-box; margin: 0; padding: 0; }
  html, body { width: 1200px; height: 800px; overflow: hidden; }
  body {
    background: var(--bg);
    font-family: "Montserrat", Arial, sans-serif;
    display: flex;
    align-items: center;
    justify-content: center;
    gap: 40px;
  }
  .card {
    position: relative;
    width: 520px;
    height: 297px;
    border-radius: 18px;
    background: var(--card);
    border-bottom: 5px solid var(--lime);
    overflow: hidden;
  }
  .card-front { display: flex; }
  .brand-side {
    width: 50%;
    display: flex;
    align-items: center;
    justify-content: center;
  }
  .brand-name {
    color: var(--white);
    font-weight: 800;
    font-size: 66px;
    letter-spacing: -1px;
  }
  .divider {
    width: 1px;
    margin: 36px 0;
    background: var(--rule);
  }
  .info-side {
    flex: 1;
    padding: 44px 0 0 30px;
    color: var(--text-soft);
    font-size: 12.5px;
    line-height: 1.55;
  }
  .person-name {
    color: var(--lime);
    font-weight: 600;
    font-size: 17px;
    letter-spacing: 0.3px;
    line-height: 1.2;
  }
  .person-title { color: var(--white); font-size: 13px; margin-bottom: 14px; }
  .address { margin-bottom: 12px; }
  .contact-list { list-style: none; }
  .contact-list li { display: flex; align-items: center; gap: 9px; }
  .contact-list svg { width: 11px; height: 11px; flex: none; fill: var(--lime); }

  .card-back { background: var(--card-dark); }
  .pattern-area {
    position: absolute;
    inset: 0;
    background: linear-gradient(135deg, #5a5d63 0%, #46494e 50%, #2f3135 100%);
  }
  .back-mark {
    position: absolute;
    right: 34px;
    bottom: 44px;
    color: var(--lime-bright);
    font-weight: 800;
    font-size: 20px;
  }
</style>
</head>
<body>
  <section class="card card-front" aria-label="Business card front">
    <div class="brand-side">
      <span class="brand-name">Brivex</span>
    </div>
    <div class="divider"></div>
    <div class="info-side">
      <p class="person-name">DANIEL REYES</p>
      <p class="person-title">President</p>
      <p class="address">4210 Harbor View Road<br>Juneau, Alaska 34812</p>
      <ul class="contact-list">
        <li><svg viewBox="0 0 12 12"><path d="M2.5 1h2l1 3-1.3 1a7 7 0 0 0 2.8 2.8l1-1.3 3 1v2a1 1 0 0 1-1 1A9.5 9.5 0 0 1 1.5 2a1 1 0 0 1 1-1z"/></svg>555-214-7730</li>
        <li><svg viewBox="0 0 12 12"><path d="M3 0h6a1 1 0 0 1 1 1v10a1 1 0 0 1-1 1H3a1 1 0 0 1-1-1V1a1 1 0 0 1 1-1zm0 1.5v8h6v-8z"/></svg>555-318-6042</li>
        <li><svg viewBox="0 0 12 12"><path d="M0 2h12v8H0zm1.2 1.2 4.8 3.4 4.8-3.4z"/></svg>info@brivex.com</li>
        <li><svg viewBox="0 0 12 12"><circle cx="6" cy="6" r="6"/></svg>www.brivex.com</li>
      </ul>
    </div>
  </section>

  <section class="card card-back" aria-label="Business card back">
    <div class="pattern-area" role="img" aria-label="Repeating embossed brand pattern in dark and mid greys"></div>
    <span class="back-mark">Brivex</span>
  </section>
</body>
</html>
```